Specialized tax accounting firm needs letterhead design

We need a letterhead design for a professional services firm called R. Everett Lund Inc. The firm is essentially a very specialized tax accounting firm - instead of serving the end consumer, we support other public accounting firms in the area of Canadian and U.S. tax advisory and compliance (i.e. they call us on tax issues too complex for the general practitioner. Our byline is "Tax Support Services for Public Accounting Firms". Our letterhead should utilize our logo and be based on colours present in our logo (see file attached). The final design needs to convey professionalism and trustworthiness (we're hired by accountants after all!) while being creative and eye-catching.

I've attached:
The font used in the logo
The logo itself in a variety of file formats
A single page showing the key firm information which should be appearing in the letterhead

Please note that there is much more leather background around the logo than needs to be incorporated in the letterhead.

Industry/Entity Type

Accounting

```html
<!DOCTYPE html>
<html lang="en">
<head>
<meta charset="utf-8">
<title>R. Everett Lund Inc. — Letterhead</title>
<link rel="stylesheet" href="https://fonts.googleapis.com/css2?family=Arimo:wght@400&family=Open+Sans:wght@400;600&display=swap">
<style>
  :root {
    --ink-black: #000000;
    --paper: #ffffff;
    --navy: #1f3a78;
    --body-ink: #2b2b2b;
    --accent-orange: #f08a1c;
    --label-ink: #111111;
  }
  * { margin: 0; padding: 0; box-sizing: border-box; }
  html, body { width: 927px; height: 1200px; overflow: hidden; background: var(--paper); }
  .letterhead {
    position: relative;
    width: 927px;
    height: 1200px;
    background: var(--paper);
    font-family: "Open Sans", Arial, sans-serif;
  }
  .masthead {
    position: absolute; left: 0; top: 0;
    width: 100%; height: 148px;
    background: var(--ink-black);
  }
  .brand {
    position: absolute; left: 249px; top: 40px;
    display: flex; align-items: center; gap: 14px;
  }
  .brand-square {
    width: 50px; height: 50px;
    background: var(--accent-orange);
  }
  .brand-text { color: var(--paper); }
  .brand-name {
    font-weight: 600;
    font-size: 30px;
    letter-spacing: 3px;
    line-height: 1.05;
    text-transform: uppercase;
  }
  .brand-tagline {
    margin-top: 6px;
    font-size: 9.6px;
    letter-spacing: 1.3px;
    text-transform: uppercase;
    padding-top: 5px;
    border-top: 1px solid var(--paper);
  }
  .recipient {
    position: absolute; left: 98px; top: 216px;
    font-size: 13px; line-height: 17.5px;
    color: var(--navy);
    text-transform: uppercase;
  }
  .role { color: var(--label-ink); margin-left: 3px; }
  .letter-body {
    position: absolute; left: 98px; top: 340px;
    width: 733px;
    font-family: "Arimo", Arial, sans-serif;
    font-size: 17.4px;
    line-height: 20.6px;
    color: var(--body-ink);
    text-align: justify;
    hyphens: auto;
  }
  .letter-body p { margin-bottom: 20.6px; }
  .sign-off {
    position: absolute; left: 99px; top: 945px;
    font-size: 13.5px; color: var(--navy);
  }
  .signature {
    position: absolute; left: 99px; top: 998px;
    font-size: 13.5px; color: var(--navy);
  }
  .sender {
    position: absolute; left: 97px; top: 1083px;
    font-size: 13.5px; color: var(--navy); text-transform: uppercase;
  }
  .sender-address {
    position: absolute; left: 97px; top: 1112px;
    font-size: 13.5px; color: var(--label-ink);
  }
  .contact {
    position: absolute; top: 1137px;
    font-size: 12.5px; line-height: 19px; color: var(--label-ink);
  }
  .contact-phone { left: 97px; }
  .contact-web { left: 342px; }
  .contact dt { color: var(--navy); display: inline; margin-right: 6px; }
  .contact dd { display: inline; }
  .footer-rule {
    position: absolute; left: 0; bottom: 0;
    width: 100%; height: 7px; background: var(--ink-black);
  }
</style>
</head>
<body>
<div class="letterhead">
  <header class="masthead">
    <div class="brand">
      <div class="brand-square"></div>
      <div class="brand-text">
        <div class="brand-name">R. Everett Lund Inc.</div>
        <div class="brand-tagline">Tax Support Services for Public Accounting Firms</div>
      </div>
    </div>
  </header>

  <address class="recipient">
    Daniel Harwood<span class="role">Owner</span><br>
    418 Elm Crest Rd.<br>
    Albany, NY 12203
  </address>

  <main class="letter-body">
    <p>Lorem ipsum dolor sit amet,</p>
    <p>Lorem ipsum dolor sit amet, consectetur adipiscing elit. Donec orci purus, luctus vitae dignissim eu, iaculis sed purus. Vivamus faucibus, ipsum nec aliquet viverra, leo mauris condimentum ligula, sit amet sagittis enim ligula quis arcu. Nam egestas tortor id nisi porttitor mattis. In tortor ante, ultricies in suscipit a, tempus non massa. Vivamus et auctor mi. Fusce vel massa nulla. Phasellus nec eros mauris, et scelerisque orci. Donec malesuada orci vitae nulla accumsan porta a id massa. Quisque accumsan iaculis magna sit amet fringilla. Maecenas consequat, magna eget tincidunt semper, odio nibh rutrum mi, id feugiat ante nisi eu risus. Vestibulum nunc orci, rhoncus a placerat in, ultricies in mi. Cras mattis varius eros, vel fringilla nisi suscipit eget.</p>
    <p>Quisque scelerisque sagittis nulla at porttitor. Mauris a justo et tellus interdum tristique. Sed id augue vitae urna euismod commodo aliquet a quam. Pellentesque arcu velit, cursus et malesuada ut, consequat et diam. Nullam erat sem, rhoncus id ullamcorper vitae, rhoncus et arcu. In ultricies ultricies nulla, ut rutrum nisi iaculis at. Donec eu magna a metus ornare faucibus. Fusce aliquet faucibus ultricies. Morbi semper, est id tincidunt gravida, sem arcu adipiscing lacus, ac bibendum nulla leo eu purus. Quisque nec diam sed risus consectetur a ccumsan quis quis nibh. Vestibulum id purus lorem.</p>
    <p>Vivamus vehicula accumsan lacinia. Aliquam erat volutpat. Pellentesque consequat venenatis velit non gravida. Etiam et sem et nulla congue aliquam sed eget augue. Nulla facilisi. Pellentesque habitant morbi tristique senectus et netus et malesuada fames ac turpis egestas. Nulla a elit at sem iaculis congue. Nullam mollis tristique lobortis.</p>
  </main>

  <p class="sign-off">Yours,</p>
  <p class="signature">Daniel Harwood</p>

  <footer>
    <p class="sender">Daniel Harwood <span class="role">Owner</span></p>
    <p class="sender-address">12-540 Harbourview Lane Halifax, Nova Scotia, Canada B3K-2T6</p>
    <dl class="contact contact-phone">
      <div><dt>PHONE:</dt><dd>555.214.3380</dd></div>
      <div><dt>FAX:</dt><dd>555.214.3390</dd></div>
    </dl>
    <dl class="contact contact-web">
      <div><dt>EMAIL:</dt><dd>office@lundtaxsupport.example</dd></div>
      <div><dt>WEB:</dt><dd>www.lundtaxsupport.example</dd></div>
    </dl>
  </footer>

  <div class="footer-rule"></div>
</div>
</body>
</html>
```